New Landing page in Wordpress Design Project

Hi we have launched a new website www.velmorewindowdrapes.co.uk and although we are doing a PPC campaign and getting a good number of hits, we are not getting enquiries. I need the website to be adjusted to improve visitor retention and I am lead to believe if your landing page is poor that is the main reason. At the moment the home page is the landing page. I am happy to amend this or add a additional landing page. My own web guru will make the necessary changes. I want to portray a top quality looking site

Industry/Entity Type

Campaign

```html
<!DOCTYPE html>
<html lang="en">
<head>
<meta charset="utf-8">
<title>Velmore Window Drapes</title>
<link rel="stylesheet" href="https://fonts.googleapis.com/css2?family=Open+Sans:wght@400;600&display=swap">
<style>
:root{
  --teal:#1f8f96;
  --teal-dark:#17747a;
  --ink:#3a3a3a;
  --muted:#6b6b6b;
  --line:#d8d8d8;
  --page:#ffffff;
  --footer:#2b2b2b;
  --footer-text:#cfcfcf;
}
*{box-sizing:border-box;margin:0;padding:0}
html,body{width:816px;height:1200px;overflow:hidden;background:var(--page)}
body{font-family:"Open Sans",Arial,sans-serif;color:var(--ink);position:relative}
.header{height:118px;position:relative}
.brand{position:absolute;left:52px;top:26px;display:flex;align-items:center;gap:10px}
.brand-mark{width:14px;height:14px;border-radius:50%;background:var(--teal)}
.brand-name{font-size:30px;font-weight:600;color:var(--teal);letter-spacing:.5px}
.search{position:absolute;right:54px;top:44px;width:168px;height:24px;border:1px solid #9a9a9a;background:#f4f4f4;display:flex;align-items:center;padding-left:6px;font-size:10px;color:#777}
.search-btn{position:absolute;right:0;top:0;width:24px;height:22px;background:#444;display:flex;align-items:center;justify-content:center}
.nav{height:24px;background:var(--teal);display:flex;align-items:center;padding-left:52px;gap:17px}
.nav a{color:#fff;font-size:10.5px;text-decoration:none;text-transform:uppercase;letter-spacing:.2px}
.nav a.active{font-weight:600}
.hero{position:relative;height:372px;background:linear-gradient(180deg,#6ec6cc 0%,#d9eef0 38%,#f4f4f2 60%,#dcdcd8 100%)}
.hero-arrow{position:absolute;top:170px;width:22px;height:36px}
.hero-arrow.left{left:8px}.hero-arrow.right{right:8px}
.dots{display:flex;justify-content:center;gap:7px;margin:12px 0 18px}
.dots span{width:8px;height:8px;border-radius:50%;background:#c8c8c8}
.dots span.on{background:var(--teal)}
.welcome{text-align:center;padding:0 110px}
.welcome h1{font-size:15px;font-weight:600;color:var(--teal);text-transform:uppercase;margin-bottom:8px}
.welcome p{font-size:10px;line-height:15px;color:var(--muted)}
.about{display:flex;gap:36px;margin:26px 52px 0}
.about-text{flex:1}
h2{font-size:15px;font-weight:400;color:var(--teal);padding-bottom:6px;border-bottom:1px solid var(--line);margin-bottom:10px}
.about-text p{font-size:9.5px;line-height:14px;color:var(--muted)}
.video{width:200px;height:118px;margin-top:10px;background:linear-gradient(180deg,#3a3a3a,#1c1c1c);position:relative}
.video-bar{position:absolute;left:0;right:0;bottom:0;height:14px;background:#111}
.lower{display:flex;gap:40px;margin:70px 52px 0}
.gallery{flex:1}
.thumbs{display:grid;grid-template-columns:repeat(3,88px);gap:12px 10px;margin-top:4px}
.thumb{height:62px;border:3px solid #fff;box-shadow:0 0 0 1px var(--line)}
.pager{display:flex;justify-content:flex-end;gap:3px;width:284px;margin-top:6px}
.pager span{width:12px;height:12px;border:1px solid #aaa;font-size:8px;display:flex;align-items:center;justify-content:center;color:#666}
.enquiry{width:262px;border:1px solid var(--line);background:#fafafa;padding:10px 14px 14px}
.enquiry h2{text-align:center}
.field{display:flex;align-items:center;margin:10px 0;font-size:9px;color:var(--muted)}
.field label{width:58px}
.field .box{flex:1;height:18px;border:1px solid #c9c9c9;background:#fff}
.field.tall{align-items:flex-start}
.field.tall .box{height:56px}
.submit{margin-left:auto;display:block;width:60px;height:18px;background:var(--teal);color:#fff;font-size:9px;border:0;text-transform:uppercase}
.footer{position:absolute;left:0;right:0;bottom:0;height:82px;background:var(--footer);padding:20px 52px}
.footer-links{font-size:9px;color:var(--footer-text);text-transform:uppercase}
.copyright{font-size:8.5px;color:#999;margin-top:8px}
.social{position:absolute;right:52px;top:18px;display:flex;gap:6px}
.social span{width:20px;height:20px;border-radius:50%}
</style>
</head>
<body>
<header class="header">
  <div class="brand"><span class="brand-mark"></span><span class="brand-name">Velmore Window Drapes</span></div>
  <div class="search">Search
    <span class="search-btn"><svg width="12" height="12" viewBox="0 0 12 12"><circle cx="5" cy="5" r="3.5" fill="none" stroke="#fff" stroke-width="1.5"/><line x1="7.6" y1="7.6" x2="11" y2="11" stroke="#fff" stroke-width="1.5"/></svg></span>
  </div>
</header>
<nav class="nav">
  <a class="active">Home</a><a>About Us</a><a>News</a><a>Curtains</a><a>Scatter Cushions &amp; Bed Throws</a><a>Gallery</a><a>Testimonials</a><a>Contact Us</a>
</nav>
<section class="hero" role="img" aria-label="Bright living room with a white sofa, patterned and lime cushions and a sea view">
  <svg class="hero-arrow left" viewBox="0 0 22 36"><polyline points="16,4 4,18 16,32" fill="none" stroke="#fff" stroke-width="3"/></svg>
  <svg class="hero-arrow right" viewBox="0 0 22 36"><polyline points="6,4 18,18 6,32" fill="none" stroke="#fff" stroke-width="3"/></svg>
</section>
<div class="dots"><span class="on"></span><span></span><span></span><span></span></div>
<section class="welcome">
  <h1>Welcome to Velmore Window Drapes</h1>
  <p>Hi my name is Helen. Velmore Window Drapes is my inspiration. I'm passionate about my fabrics and take pride in what I do. I've always enjoyed creating the WOW factor. Designer curtains have never looked so good!</p>
</section>
<section class="about">
  <div class="about-text">
    <h2>About Velmore Drapes</h2>
    <p>Choose from the designer curtain collections by browsing our range of swatch books for something modern or contemporary, dramatic and vintage or stylish children's fabrics – you'll be spoilt for choice! Once you've found your perfect fabric, it's on to the curtain heading and we have plenty of choices there too; pick from pencil pleat, eyelet or pinch pleat. Pencil pleat heading curtains have classic appeal hanging in a refined and tasteful style at the window. For a streamlined look, eyelet headings are modern and classy. Pinch pleat curtains are the ultimate choice for a sophisticated and luxurious feel.</p>
  </div>
  <div class="video" role="img" aria-label="Introduction video player"><div class="video-bar"></div></div>
</section>
<section class="lower">
  <div class="gallery">
    <h2>Photo Gallery</h2>
    <div class="thumbs">
      <div class="thumb" role="img" aria-label="Green armchair" style="background:linear-gradient(#5b6b3e,#3e4a2a)"></div>
      <div class="thumb" role="img" aria-label="Grey sofa with cushions" style="background:linear-gradient(#9a9a98,#6d6d6b)"></div>
      <div class="thumb" role="img" aria-label="Striped curtains" style="background:linear-gradient(90deg,#c9b89a,#8f7e66)"></div>
      <div class="thumb" role="img" aria-label="Patterned cushions" style="background:linear-gradient(#a8a8b0,#d8d8dc)"></div>
      <div class="thumb" role="img" aria-label="Lime cushions" style="background:linear-gradient(#d6df6a,#b6c24a)"></div>
      <div class="thumb" role="img" aria-label="Pink and teal cushions" style="background:linear-gradient(90deg,#d98aa8,#5ab3b0)"></div>
    </div>
    <div class="pager"><span>‹</span><span>›</span></div>
  </div>
  <form class="enquiry">
    <h2>Enquiry Form</h2>
    <div class="field"><label>Name :</label><span class="box"></span></div>
    <div class="field"><label>Email :</label><span class="box"></span></div>
    <div class="field"><label>Phone :</label><span class="box"></span></div>
    <div class="field tall"><label>Message :</label><span class="box"></span></div>
    <button class="submit" type="button">Submit</button>
  </form>
</section>
<footer class="footer">
  <div class="footer-links">Home | About Us | News | Curtains | Scatter Cushions &amp; Bed Throws | Gallery | Contact Us | Testimonials</div>
  <div class="copyright">© 2013 Copyrights Velmore Window Drapes All Rights Reserved.</div>
  <div class="social"><span style="background:#3b5b98"></span><span style="background:#2aa9e0"></span><span style="background:#d23a2c"></span></div>
</footer>
</body>
</html>
```